Luxury Wine Label for New Startup Winery

We need a wine label for our new winery startup. We have worked with a local designer but do not feel the resulting label / logo have the elevation required to present our brand as a luxury wine. Our winery is called "Harrowgate Vineyards" and we are focused on extremely high quality hand crafted artisan and estate wines from the Pacific Northwest.
We would like to see designs that utilize a tree line, or other imagery that represents the "Harrowgate" part of our company name. Another interesting feature could be wood grain.
A logo will be required based on your design so please design with this in mind:
This logo should be consistent with the wine bottle label design, and should be representative of our high end exclusive wine while giving a sense of place (Oregon/ Pacific Northwest.)
I will supply an image of the design we received from our local designer, PLEASE NOTE: in general we do like wood grain and tree line concepts but feel the execution was poorly done.
ATTN: Logo design should be suitable for use on: Bottles (Red wine/rose/white wine), Bussiness cards, vehicle signage, business signage, etc
P.S.:
If you have a design that is not outside the box we are still interested in seeing it.
Label is for a burgundy style bottle with a label height of 3.5 - 4" and a width of 3.5-4"
any label <= 4"x4" and >=3.5"x3.5" will be acceptable:
HOWEVER Width should be greater than or equal to height due to the bottle format
Target Market(s)
Wine enthusiasts with adequate discretionary budgets to afford $100 bottles of wine.
Industry/Entity Type
Wine / Winery
Requirements
Must have
- A sense of luxury, a feel of exclusivity, and a theme consistent with our product and brand name
Nice to have
- Tree line, wood grain or other wood themes. Serif fonts
Should not have
- anything cheesy, off topic, hard to read script fonts or anything that makes the label hard to read from a few feet away or too busy

```html
<!DOCTYPE html>
<html lang="en">
<head>
<meta charset="utf-8">
<title>Harrowgate Vineyards — Wine Label</title>
<link rel="stylesheet" href="https://fonts.googleapis.com/css2?family=Cormorant+Garamond:wght@400;500;600&family=Great+Vibes&display=swap">
<style>
  :root {
    --page-bg: #f5f5f5;
    --ink: #1e1a16;
    --ink-soft: #4a4440;
    --accent: #b8692a;
    --mark-warm: #f0a23a;
    --mark-red: #e8401c;
    --mark-dark: #2a2320;
    --walnut-dark: #5a3a22;
    --walnut-mid: #8a5a34;
    --walnut-light: #b98a5a;
    --rule: #6b625b;
  }
  * { box-sizing: border-box; margin: 0; padding: 0; }
  html, body {
    width: 1200px;
    height: 999px;
    overflow: hidden;
    background: var(--page-bg);
  }
  .canvas {
    position: relative;
    width: 1200px;
    height: 999px;
    display: flex;
    justify-content: center;
    align-items: center;
  }
  .label {
    width: 540px;
    display: flex;
    flex-direction: column;
    align-items: center;
    font-family: "Cormorant Garamond", serif;
    font-weight: 500;
    color: var(--ink);
    text-align: center;
  }
  .label__emblem {
    width: 240px;
    height: 240px;
    border-radius: 50%;
    background: radial-gradient(circle at 42% 40%, var(--mark-warm) 0%, var(--mark-red) 62%, var(--mark-dark) 100%);
    margin-bottom: 30px;
  }
  .label__name {
    font-size: 62px;
    line-height: 1.02;
    letter-spacing: 0.06em;
    font-weight: 500;
    text-transform: uppercase;
  }
  .label__grain {
    margin-top: 18px;
    width: 300px;
    height: 6px;
    border-radius: 3px;
    background: linear-gradient(90deg, var(--walnut-dark), var(--walnut-light) 30%, var(--walnut-mid) 55%, var(--walnut-light) 78%, var(--walnut-dark));
  }
  .label__tagline {
    margin-top: 16px;
    font-size: 30px;
    letter-spacing: 0.08em;
    color: var(--accent);
    text-transform: uppercase;
  }
  .label__details {
    margin-top: 14px;
    display: grid;
    grid-template-columns: 1fr 1fr;
    width: 440px;
  }
  .detail {
    display: flex;
    flex-direction: column;
    align-items: flex-start;
    padding: 0 20px;
  }
  .detail + .detail { border-left: 1.5px solid var(--rule); }
  .detail__title {
    font-size: 23px;
    letter-spacing: 0.04em;
    text-transform: uppercase;
    white-space: nowrap;
  }
  .detail__field-label {
    margin-top: 8px;
    font-size: 15px;
    letter-spacing: 0.06em;
    text-transform: uppercase;
    color: var(--ink-soft);
  }
  .detail__field {
    margin-top: 6px;
    width: 160px;
    height: 32px;
    border: 1px solid var(--rule);
    display: flex;
    align-items: center;
    justify-content: center;
  }
  .detail__signature {
    font-family: "Great Vibes", cursive;
    font-size: 24px;
    color: var(--ink);
  }
  .label__footer {
    margin-top: 28px;
    display: flex;
    align-items: baseline;
    gap: 20px;
    text-transform: uppercase;
  }
  .footer__origin, .footer__abv {
    font-size: 15px;
    letter-spacing: 0.06em;
    color: var(--ink-soft);
  }
  .footer__volume { font-size: 30px; font-weight: 500; }
</style>
</head>
<body>
  <main class="canvas">
    <section class="label">
      <div class="label__emblem" role="img" aria-label="Painted brushstroke emblem in orange, red and black"></div>
      <h1 class="label__name">Harrowgate<br>Vineyards</h1>
      <div class="label__grain" aria-hidden="true"></div>
      <p class="label__tagline">Hand Crafted</p>
      <div class="label__details">
        <div class="detail">
          <span class="detail__title">Estate Grown</span>
          <span class="detail__field-label">Vintage</span>
          <span class="detail__field"></span>
        </div>
        <div class="detail">
          <span class="detail__title">Willamette</span>
          <span class="detail__field-label">Winemaker</span>
          <span class="detail__field"><span class="detail__signature">Ellis Rourke</span></span>
        </div>
      </div>
      <div class="label__footer">
        <span class="footer__origin">Product of Oregon</span>
        <span class="footer__volume">750 ML</span>
        <span class="footer__abv">13.5% Alc./Vol.</span>
      </div>
    </section>
  </main>
</body>
</html>
```